Honey apple cider vinegar label

organic food company need a contemporary honey apple cider vinegar and honey vinegar label, natural GMP logo HACCP LOgo
label detail height :140mm Width:80mm
ingredient: honey, apple cider vinegar and water, free from artificial color & preservative
Shelf Life: 3 years
Net weight 400ml
Storage : store in cool place , do not expose to sunlight
instruction for use: add 20ml to a full glass of water 3, times a days before meal, stop consuming if allergies happen
certification, GMP HACCP, Halal, natural product

Target Market(s)

health conscious group

Requirements
Must have
• modern feel, honey and apple picture

```html
<!DOCTYPE html>
<html lang="en">
<head>
<meta charset="utf-8">
<title>Meadowmere Apple Cider Vinegar &amp; Honey Label</title>
<link href="https://fonts.googleapis.com/css2?family=Anton&family=Roboto:wght@400;500;700&display=swap" rel="stylesheet">
<style>
  :root {
    --backdrop: #e9ecea;
    --label: #ffffff;
    --ink: #1d1d1b;
    --honey: #f6b817;
    --apple-red: #e0412f;
    --apple-orange: #f28a3c;
    --leaf-green: #4caf3a;
    --brand-ink: #2c2a5a;
    --badge-line: #3b8f3e;
    --badge-blue: #1f6fb5;
  }
  * { margin: 0; padding: 0; box-sizing: border-box; }
  html, body { width: 825px; height: 1200px; overflow: hidden; }
  body {
    background: var(--backdrop);
    font-family: "Roboto", Arial, sans-serif;
    color: var(--ink);
    position: relative;
  }
  .label {
    position: absolute;
    left: 92px; top: 36px;
    width: 641px; height: 1127px;
    background: var(--label);
    overflow: hidden;
  }
  .honey-dipper-art {
    position: absolute;
    left: 18px; top: 0;
    width: 120px; height: 360px;
    border-radius: 0 0 60px 60px;
    background: linear-gradient(180deg, #a85a22 0%, #d98c2e 45%, #f6c54a 100%);
  }
  .brand {
    position: absolute;
    left: 195px; top: 44px;
    width: 260px;
    text-align: center;
  }
  .brand-dot {
    display: block;
    width: 50px; height: 50px;
    margin: 0 auto 10px;
    border-radius: 50%;
    background: var(--brand-ink);
  }
  .brand-name {
    font-weight: 700;
    font-size: 32px;
    color: var(--brand-ink);
    line-height: 1;
  }
  .certifications {
    position: absolute;
    left: 534px; top: 22px;
  }
  .cert-badge { display: block; margin-bottom: 16px; }
  .title {
    position: absolute;
    left: 0; width: 100%;
    text-align: center;
    font-family: "Anton", Impact, sans-serif;
    font-weight: 400;
    font-size: 114px;
    line-height: 1;
    letter-spacing: 8px;
    text-transform: uppercase;
  }
  .title-apple { top: 157px; }
  .title-cider { top: 300px; }
  .title-vinegar { top: 442px; }
  .title-honey { top: 552px; color: var(--honey); font-size: 104px; }
  .ingredients-bar {
    position: absolute;
    left: 0; top: 694px;
    width: 100%; height: 36px;
    background: var(--ink);
    color: #fff;
    font-size: 23px;
    font-weight: 500;
    line-height: 36px;
    text-align: center;
  }
  .free-from {
    position: absolute;
    left: 0; top: 740px; width: 100%;
    text-align: center;
    font-size: 23px;
    font-weight: 700;
  }
  .apple-art {
    position: absolute;
    left: 400px; top: 790px;
    width: 241px; height: 320px;
    border-radius: 50% 0 0 50%;
    background: radial-gradient(circle at 45% 50%, var(--apple-orange) 0%, var(--apple-red) 60%, #b52a22 100%);
  }
  .usage {
    position: absolute;
    left: 18px; top: 808px;
    font-size: 21px;
    line-height: 30px;
  }
  .usage-heading { font-weight: 700; }
  .usage .warning { text-decoration: underline; }
  .storage {
    position: absolute;
    left: 18px; top: 962px;
    font-size: 21px;
    line-height: 29px;
  }
  .net-weight {
    position: absolute;
    left: 225px; top: 1076px;
    font-size: 21px;
  }
  .natural-badge { position: absolute; left: 515px; top: 985px; }
</style>
</head>
<body>
  <main class="label">
    <div class="honey-dipper-art" role="img" aria-label="Wooden honey dipper dripping golden honey"></div>

    <div class="brand">
      <span class="brand-dot"></span>
      <div class="brand-name">Meadowmere</div>
    </div>

    <div class="certifications">
      <svg class="cert-badge" width="64" height="64" viewBox="0 0 64 64" aria-hidden="true"><circle cx="32" cy="32" r="29" fill="#fff" stroke="var(--badge-line)" stroke-width="3"/><circle cx="32" cy="32" r="18" fill="var(--badge-line)"/></svg>
      <svg class="cert-badge" width="64" height="64" viewBox="0 0 64 64" aria-hidden="true"><circle cx="32" cy="32" r="29" fill="#fff" stroke="var(--badge-blue)" stroke-width="3"/><circle cx="32" cy="32" r="18" fill="var(--badge-blue)"/></svg>
      <svg class="cert-badge" width="64" height="64" viewBox="0 0 64 64" aria-hidden="true"><circle cx="32" cy="32" r="28" fill="#fff" stroke="var(--ink)" stroke-width="3"/></svg>
    </div>

    <h1>
      <span class="title title-apple">Apple</span>
      <span class="title title-cider">Cider</span>
      <span class="title title-vinegar">Vinegar</span>
      <span class="title title-honey">&amp; Honey</span>
    </h1>

    <div class="ingredients-bar">Ingredients: honey, apple cider vinegar and water</div>
    <p class="free-from">Free from artificial colors &amp; preservatives</p>

    <div class="apple-art" role="img" aria-label="Sliced red apple with green leaf"></div>

    <div class="usage">
      <p class="usage-heading">Instructions of use:</p>
      <p>Add <strong>20ml</strong> to a full glass of water.</p>
      <p>Drink 3 times a days before a meal.</p>
      <p class="warning">Stop consuming if allergies happen.</p>
    </div>

    <div class="storage">
      <p>Store in a cool place</p>
      <p>Do not expose to sunlight</p>
      <p>Shelf Life: 3 years</p>
    </div>

    <p class="net-weight">Net weight 400ml</p>

    <svg class="natural-badge" width="104" height="104" viewBox="0 0 104 104" aria-hidden="true"><circle cx="52" cy="52" r="50" fill="var(--leaf-green)"/></svg>
  </main>
</body>
</html>
```